Mandala-like Graphic for Ecosystem of Well-Being

I have created a simple graphic for a framework I use with clients and potential clients. I would like it to look more polished, professional, and customized. (As opposed to non-graphic designer created it on Canva or Powrepoint) I would like to possibly integrate my brand colors---or one of my brand colors. https://huechartly.org/scheme-7158/ The dark blue is the one to definitely use. I do not want it looking to feminine. I do want different colors for the 5 elements: Purpose, Mental, Physical, Emotional, Social.

Target Market(s)

Working professionals.

Font styles to use
Serif
Other font styles liked:
• Playfair Display

Requirements
Must have
• 4 Overlapping circles with one circle in center that says Purpose
Other 4 circles labeled Physical, Emotional, Mental, Social
Mandala-like design

**I added an attachment with colors I use when marketing this course.**
Nice to have
• Playfair Display font

```html
<!DOCTYPE html>
<html lang="en">
<head>
<meta charset="utf-8">
<title>Ecosystem of Well-Being</title>
<link rel="stylesheet" href="https://fonts.googleapis.com/css2?family=Tinos:wght@700&display=swap">
<style>
  :root {
    --canvas: #ffffff;
    --mental: #18b7e3;
    --social: #fcc111;
    --emotional: #80c454;
    --physical: #cd58a0;
    --purpose: #161f4b;
    --label: #ffffff;
    --gap: #ffffff;
  }
  html, body {
    margin: 0;
    padding: 0;
    width: 1200px;
    height: 1200px;
    overflow: hidden;
    background: var(--canvas);
  }
  .wellbeing-ecosystem {
    display: block;
    width: 1200px;
    height: 1200px;
  }
  .petal { stroke: var(--gap); stroke-width: 12; }
  .petal--mental { fill: var(--mental); }
  .petal--social { fill: var(--social); }
  .petal--emotional { fill: var(--emotional); }
  .petal--physical { fill: var(--physical); }
  .core { fill: var(--purpose); }
  .label {
    font-family: "Tinos", "Times New Roman", serif;
    font-weight: 700;
    font-size: 62px;
    letter-spacing: 1px;
    fill: var(--label);
    text-anchor: middle;
  }
</style>
</head>
<body>
<svg class="wellbeing-ecosystem" viewBox="0 0 1932 1932" role="img" aria-label="Ecosystem of Well-Being: Purpose at the centre, surrounded by Mental, Social, Emotional and Physical">
  <defs>
    <clipPath id="upper-left-quadrant">
      <rect x="0" y="0" width="961" height="966"/>
    </clipPath>
  </defs>

  <g class="petals">
    <circle class="petal petal--mental" cx="961" cy="693" r="272"/>
    <circle class="petal petal--social" cx="1234" cy="966" r="272"/>
    <circle class="petal petal--emotional" cx="961" cy="1239" r="272"/>
    <circle class="petal petal--physical" cx="688" cy="966" r="272"/>
    <circle class="petal petal--mental" cx="961" cy="693" r="272" clip-path="url(#upper-left-quadrant)"/>
  </g>

  <circle class="core" cx="961" cy="966" r="175"/>

  <g class="labels">
    <text class="label" x="961" y="663">MENTAL</text>
    <text class="label" x="603" y="984">PHYSICAL</text>
    <text class="label" x="961" y="984">PURPOSE</text>
    <text class="label" x="1334" y="984">SOCIAL</text>
    <text class="label" x="961" y="1310">EMOTIONAL</text>
  </g>
</svg>
</body>
</html>
```